Brightvale Marketing Banner for emails to customers

Hi Marketing Team The information is to be a nice banner say half page on Marketing our Services to prospective customers, this is embedded into an email so something nice with the content that I will provide. Based on a nice background to highlight our service portfolio aligned to our website
www.brightvale.com.au

```html
<!DOCTYPE html>
<html lang="en">
<head>
<meta charset="utf-8">
<title>Brightvale – Services Banner</title>
<link rel="stylesheet" href="https://fonts.googleapis.com/css2?family=Tinos:wght@400;700&family=Open+Sans:wght@400;600&display=swap">
<style>
  :root {
    --navy: #17407a;
    --navy-deep: #123566;
    --orange: #f36a21;
    --sky: #6f8fbf;
    --white: #ffffff;
    --ink: #2b2b2b;
    --wall: #f1f1f0;
    --floor: #d9d9d7;
    --page: #a7a7a7;
  }
  * { margin: 0; padding: 0; box-sizing: border-box; }
  html, body { width: 900px; height: 1200px; overflow: hidden; background: var(--page); }
  .canvas { position: relative; width: 900px; height: 1200px; }

  .banner {
    position: absolute; left: 20px; top: 312px;
    width: 695px; height: 465px;
    transform: scale(1.2374); transform-origin: top left;
    overflow: hidden;
    background: var(--wall);
    box-shadow: 0 6px 18px rgba(0,0,0,.35);
    font-family: "Open Sans", sans-serif;
  }
  .backdrop {
    position: absolute; inset: 0;
    background: linear-gradient(180deg, #f7f7f6 0%, #ececeb 78%, var(--floor) 82%, #ededec 100%);
  }
  .shapes { position: absolute; inset: 0; }

  .photo { position: absolute; }
  .photo-worker { left: 62px; top: 112px; width: 140px; height: 330px; border-radius: 60px 60px 10px 10px;
    background: linear-gradient(180deg, #e9e4df 0%, #2f4a36 45%, #1f3526 100%); }
  .photo-vacuum { left: 2px; top: 322px; width: 68px; height: 122px; border-radius: 12px;
    background: linear-gradient(180deg, #b9bcbf 0%, #6d7175 70%, #2a2a2a 100%); }
  .photo-supplies { left: 392px; top: 350px; width: 112px; height: 104px; border-radius: 14px;
    background: linear-gradient(160deg, #6fb6e6 0%, #f2d23a 45%, #3c7fd0 100%); }

  .brand {
    position: absolute; left: 360px; top: 22px;
    display: flex; align-items: center; gap: 8px;
  }
  .brand-dot { width: 26px; height: 26px; border-radius: 50%; background: var(--navy); }
  .brand-name { font-family: "Tinos", serif; font-size: 31px; color: var(--orange); line-height: 1; }

  .headline {
    position: absolute; left: 296px; top: 70px; width: 392px; height: 90px;
    border: 1.5px dashed var(--orange); border-radius: 12px; padding: 4px;
  }
  .headline-inner {
    width: 100%; height: 100%; background: var(--navy); border-radius: 9px;
    color: var(--white); font-family: "Tinos", serif; text-align: center;
    padding-top: 8px;
  }
  .headline-lead { font-size: 11.5px; letter-spacing: .3px; }
  .headline-main { font-size: 20.5px; font-weight: 700; display: flex; align-items: center; justify-content: center; gap: 5px; margin-top: 2px; }
  .years-badge { width: 28px; height: 28px; border-radius: 50%; background: var(--white); color: var(--orange);
    font-size: 17px; display: inline-flex; align-items: center; justify-content: center; }
  .headline-sub { font-size: 18px; margin-top: -1px; }

  .section-bar {
    position: absolute; left: 330px; width: 370px; height: 21px;
    font-family: "Tinos", serif; font-weight: 700; font-size: 14.5px; color: var(--white);
    padding-left: 40px; line-height: 21px; border-radius: 11px 0 0 11px;
  }
  .bar-portfolio { top: 182px; background: var(--orange); box-shadow: 0 -4px 0 var(--navy); }
  .bar-portfolio .accent { color: var(--navy); }
  .bar-upgrades { top: 262px; background: var(--navy); box-shadow: 0 -4px 0 var(--orange); }
  .bar-upgrades .accent { color: var(--orange); }

  .list { position: absolute; list-style: none; font-size: 8.3px; color: var(--ink); }
  .list li { position: relative; padding-left: 15px; }
  .list li::before { content: ""; position: absolute; left: 1px; top: 2px; width: 8px; height: 8px; border-radius: 50%; }
  .services li { margin-bottom: 8px; }
  .services li::before { background: var(--orange); }
  .services-left { left: 252px; top: 216px; }
  .services-right { left: 470px; top: 216px; }
  .divider { position: absolute; left: 463px; top: 216px; width: 1px; height: 30px; background: #b5b5b5; }
  .upgrades li { line-height: 18px; }
  .upgrades li::before { background: var(--navy); top: 5px; }
  .upgrades-left { left: 222px; top: 292px; }
  .upgrades-right { left: 455px; top: 292px; width: 225px; }
  .upgrades-right li { line-height: 11.5px; }
  .upgrades-right li::before { top: 2px; }

  .call {
    position: absolute; left: 535px; top: 364px; width: 150px; text-align: center;
    font-family: "Tinos", serif; color: var(--white);
  }
  .call-lead { font-size: 16px; line-height: 1; }
  .call-today { font-size: 22px; color: var(--orange); line-height: 1.05; }
  .call-phone { font-size: 18px; line-height: 1.1; }
  .call-email { font-size: 7.5px; letter-spacing: .6px; font-variant: small-caps; margin-top: 3px; }
</style>
</head>
<body>
<div class="canvas">
  <section class="banner">
    <div class="backdrop" role="img" aria-label="Photo backdrop of a white brick wall above pale timber floorboards"></div>

    <svg class="shapes" viewBox="0 0 695 465" width="695" height="465" aria-hidden="true">
      <path d="M36 0 H92 Q60 70 52 150 L0 170 V0 Z" fill="var(--navy)"/>
      <path d="M0 300 Q60 330 90 465 H0 Z" fill="var(--navy)"/>
      <circle cx="142" cy="140" r="128" fill="var(--orange)"/>
      <circle cx="142" cy="128" r="96" fill="var(--white)" stroke="var(--navy)" stroke-width="9"/>
      <circle cx="610" cy="420" r="86" fill="var(--sky)" opacity=".75"/>
      <circle cx="610" cy="420" r="76" fill="var(--navy-deep)"/>
      <circle cx="610" cy="420" r="71" fill="none" stroke="var(--orange)" stroke-width="1.5"/>
    </svg>

    <div class="photo photo-worker" role="img" aria-label="Photo of a cleaner in green overalls and yellow gloves vacuuming the floor"></div>
    <div class="photo photo-vacuum" role="img" aria-label="Photo of a steel wet-and-dry vacuum cleaner"></div>

    <div class="brand">
      <span class="brand-dot"></span>
      <span class="brand-name">Brightvale</span>
    </div>

    <div class="headline">
      <div class="headline-inner">
        <p class="headline-lead">BRIGHTVALE HAS BEEN IN BUSINESS FOR</p>
        <p class="headline-main"><span class="years-badge">15</span>YEARS AND BUILT A STRONG</p>
        <p class="headline-sub">and steady market reputation</p>
      </div>
    </div>

    <h2 class="section-bar bar-portfolio">PORTFOLIO OF <span class="accent">SERVICES:</span></h2>
    <ul class="list services services-left">
      <li>Equipment Sundae Machine Cleaning Service.</li>
      <li>Detailed Kitchen Cleaning and Vat Boil Outs</li>
    </ul>
    <div class="divider"></div>
    <ul class="list services services-right">
      <li>Gurney High Pressure and Playground Cleaning</li>
      <li>General Facility Maintenance</li>
    </ul>

    <h2 class="section-bar bar-upgrades"><span class="accent">BUSINESS</span> UPGRADES COMPLETED</h2>
    <ul class="list upgrades upgrades-left">
      <li>We have upgraded and digitalised our reporting system</li>
      <li>for transparency across our services - Copy Attached.</li>
    </ul>
    <ul class="list upgrades upgrades-right">
      <li>We have upgraded and digitalised our reporting system for transparency across our services - Copy Attached.</li>
    </ul>

    <div class="photo photo-supplies" role="img" aria-label="Photo of a bucket of cleaning supplies with spray bottles, sponges and gloves"></div>

    <div class="call">
      <p class="call-lead">CALL US</p>
      <p class="call-today">TODAY</p>
      <p class="call-phone">1300 555 018</p>
      <p class="call-email">service@brightvale.com.au</p>
    </div>
  </section>
</div>
</body>
</html>
```